Bref créative |
Website for Statistical Consulting Company | ||
Garnet Heron Analytics Group | ||
Consulting | ||
www.garnetheronanalyticsgroup.example | ||
We are a new company looking to focus on sound research design, cogent analysis and clear presentation of our methods and findings. | ||
Dislikes: Websites that are hard to navigate (overly complex, similar content in many different places, etc) |
Cutting-Edge Clean/Simple Professional Exciting Corporate Progressive Service Oriented Masculine |
Times New Roman Georgia |
top | ||
http://www.brivask.example/ | ||
http://www.quorimesh.example/ | ||
http://palvendrift.example/ | ||
I like it when the Nav is either on the top, left, or both. I think a theme based on the owl, which incorporates trees, would be nice, but don't feel like you have to use this idea. Follow your vision! Please don't feel too limited by this brief. Feel free to try anything! I look forward to seeing lots of different ideas |

```html
<!DOCTYPE html>
<html lang="en">
<head>
<meta charset="utf-8">
<title>Garnet Heron Analytics Group</title>
<link href="https://fonts.googleapis.com/css2?family=Cinzel:wght@400;700&family=Arimo:wght@400;700&display=swap" rel="stylesheet">
<style>
:root{
  --page:#e9e9e9;
  --red:#b3141b;
  --red-dark:#7d0a0e;
  --ink:#2b2b2b;
  --muted:#666;
  --panel:#ffffff;
  --box:#f1f1f1;
  --footer:#1a1a1a;
  --footer-text:#9a9a9a;
  --orange:#f08a12;
  --slide-dark:#0b0f24;
}
*{box-sizing:border-box;margin:0;padding:0}
html,body{width:1200px;height:1004px;overflow:hidden}
body{background:var(--page);font-family:Arimo,Arial,sans-serif;color:var(--ink);position:relative}
.abs{position:absolute}
.red-band{left:0;top:95px;width:1200px;height:300px;background:linear-gradient(#c01a20,var(--red-dark));}
.logo{left:218px;top:14px;font-family:Cinzel,serif;color:#222}
.logo .name{font-size:38px;font-weight:700;letter-spacing:2px}
.logo .sub{font-size:12px;letter-spacing:4px;margin-left:70px}
.top-social{left:905px;top:10px;display:flex;gap:7px}
.top-social span{width:11px;height:11px;border-radius:50%;background:#888}
.contact-line{left:626px;top:64px;font-size:13px;display:flex;gap:18px;align-items:center}
.contact-line .phone{font-size:18px}
.nav{left:237px;top:103px;width:729px;height:40px;background:linear-gradient(#fdfdfd,#dcdcdc);border-radius:3px;display:flex;align-items:center;padding-left:10px;gap:6px;box-shadow:0 2px 4px rgba(0,0,0,.3)}
.nav a{font-family:Cinzel,serif;font-size:14px;color:#333;text-decoration:none;padding:6px 14px;border-right:1px solid #ccc}
.nav a.active{background:var(--red);color:#fff;border-radius:2px}
.slider{left:237px;top:155px;width:729px;height:235px;border:4px solid #fff;background:#fff;box-shadow:0 3px 8px rgba(0,0,0,.4)}
.slide-art{position:absolute;left:0;top:0;width:533px;height:227px;background:radial-gradient(circle at 75% 40%,#3b4a9a,#1b2254 40%,var(--slide-dark) 75%)}
.slide-text{position:absolute;left:533px;top:0;width:188px;height:227px;background:linear-gradient(135deg,#d8232a,var(--red-dark));color:#fff;padding:18px 12px}
.slide-text h2{font-family:Cinzel,serif;font-size:19px;font-weight:400;line-height:1.25}
.slide-text p{font-size:11px;line-height:1.4;margin-top:10px}
.btn{display:inline-block;margin-top:14px;background:linear-gradient(#ffb23a,var(--orange));color:#222;font-size:13px;padding:6px 12px;border-radius:3px;font-weight:700}
.dots{left:575px;top:388px;display:flex;gap:5px;background:#fff;padding:4px 8px;border-radius:0 0 8px 8px}
.dots span{width:11px;height:11px;border-radius:50%;background:#777}
.dots span.on{background:var(--red)}
.content{left:237px;top:408px;width:729px;height:449px;background:var(--panel)}
.welcome{left:245px;top:438px;width:710px}
.welcome h1{font-family:Cinzel,serif;font-size:19px;font-weight:400}
.welcome h1 b{color:var(--red);font-weight:400}
.welcome p{font-size:11px;line-height:1.45;color:#444;margin-top:8px}
.box{top:545px;width:217px;height:205px;background:var(--box);border:1px solid #ddd;padding:12px;box-shadow:0 3px 6px rgba(0,0,0,.2)}
.box h3{font-family:Cinzel,serif;font-size:14px;font-weight:400;margin-bottom:10px}
.box h3 b{color:var(--red);font-weight:400}
.box p,.box li{font-size:10px;line-height:1.45;color:#555}
.box ul{list-style:none}
.box li{border-bottom:1px solid #ddd;padding:3px 0}
.box .more{font-size:10px;color:var(--red);margin-top:8px}
.chart{width:88px;height:78px;float:left;margin-right:8px;background:linear-gradient(135deg,#f4d23c,#d9482b);}
.news .date{color:var(--red);font-size:11px;font-weight:700}
.clients{left:237px;top:772px;width:729px;height:58px;background:linear-gradient(#fff,#e5e5e5);border:1px solid #ccc;display:flex;align-items:center;justify-content:space-around;padding:0 40px}
.clients span{font-size:22px;font-weight:700;color:#666}
.clients .arrow{position:absolute;top:16px;width:22px;height:24px;background:var(--red);color:#fff;font-size:14px;text-align:center;line-height:24px}
.trees{left:0;top:700px;width:1200px;height:160px;background:linear-gradient(transparent,#3a3a3a 75%,#111);opacity:.55}
.footer{left:0;top:857px;width:1200px;height:147px;background:var(--footer);color:var(--footer-text);font-size:10px}
.footer h4{font-family:Cinzel,serif;color:var(--red);font-size:12px;margin-bottom:8px;font-weight:700}
.col{position:absolute;top:22px;line-height:1.9}
.social{display:flex;gap:8px;flex-wrap:wrap;width:80px}
.social span{width:30px;height:30px;border-radius:50%;background:#555}
.f-logo{font-family:Cinzel,serif;color:#777;font-size:20px;font-weight:700}
</style>
</head>
<body>
<div class="abs red-band"></div>
<div class="abs logo"><div class="name">Garnet Heron</div><div class="sub">Analytics Group</div></div>
<div class="abs top-social"><span></span><span></span><span></span></div>
<div class="abs contact-line"><span>✉ info@garnetheronanalyticsgroup.example</span><span class="phone">☎ 123.456.7890</span></div>
<nav class="abs nav"><a class="active">Home</a><a>About Us</a><a>Services</a><a>Clients</a><a>Resources</a><a>Latest News</a><a style="border:none">Contact Us</a></nav>
<div class="abs slider">
  <div class="slide-art" role="img" aria-label="Glowing three dimensional data surface chart on a dark blue background"></div>
  <div class="slide-text"><h2>Garnet Heron<br>Analytics Group</h2><p>Clear research design, cogent analysis and plain presentation of methods and findings for every client project we take on.</p><span class="btn">Learn more ›</span></div>
</div>
<div class="abs dots"><span class="on"></span><span></span><span></span><span></span></div>
<div class="abs content"></div>
<div class="abs welcome"><h1>Welcome to <b>Garnet Heron Analytics Group</b></h1>
<p>We help organisations ask better questions of their data. From study design through sampling, modelling and reporting, our consultants keep every step transparent so decisions rest on evidence you can trust. We work with research teams, public bodies and businesses of all sizes, and we explain our methods in plain language. Each engagement ends with clear findings, tidy documentation and practical advice on the next steps for your work.</p></div>
<div class="abs box" style="left:245px"><h3>Who <b>we are</b></h3><div class="chart" role="img" aria-label="Colourful 3D statistical surface chart"></div><p>A small team of statisticians focused on careful design and honest reporting of results.</p><div class="more" style="clear:both">» Read more</div></div>
<div class="abs box" style="left:492px"><h3>What <b>we do</b></h3><ul><li>Study design and sampling plans</li><li>Regression and survey analysis</li><li>Forecasting and trend models</li><li>Data cleaning and auditing</li><li>Reports and presentations</li></ul><div class="more">» Read more</div></div>
<div class="abs box news" style="left:740px"><h3>Latest <b>News</b></h3><div class="date">10-09-2013</div><p>New survey analysis service now open for booking.</p><br><div class="date">10-09-2013</div><p>Our team joins a regional health study project.</p><div class="more">» Read more</div></div>
<div class="abs trees" role="img" aria-label="Silhouette of a forest tree line"></div>
<div class="abs clients"><div class="arrow" style="left:6px">‹</div><span>Tovrella</span><span>Kessmar</span><span>Dunvale Energy</span><span>Ostrik</span><span>Linaro Tel</span><div class="arrow" style="right:6px">›</div></div>
<footer class="abs footer">
  <div class="col" style="left:245px"><h4>Navigation</h4>Home<br>About Us<br>Services<br>Clients</div>
  <div class="col" style="left:320px"><h4>&nbsp;</h4>Resources<br>Latest News<br>Contact Us</div>
  <div class="col" style="left:408px"><h4>Contact Us</h4>Address: Line 1<br>Address: Line 2<br>Phone: 123.456.7890<br>Email: info@garnetheronanalyticsgroup.example</div>
  <div class="col" style="left:631px"><h4>Follow Us</h4><div class="social"><span></span><span></span><span></span><span></span></div></div>
  <div class="col" style="left:775px"><div class="f-logo">Garnet Heron</div>© 2013, Garnet Heron Analytics Group.<br>All rights reserved.</div>
</footer>
</body>
</html>
```